Cruise price comparison web design project

The project's name is Wellenfuchsportal.
www.wellenfuchsportal.de
The current design (which I don't really like) can be found here:
http://wfp02.wellenfuchsportal.de/

I m not too happy with what the current developers have been done so far (in terms of design), so I hope to find a great designer her to develop a design that kicks arses. : )

We are currently developing a site for the German market that brings travel agents and cruise holiday makers together. We are not an ordinary travel agency.
Wellenfuchsportal is a quick and convenient way to have independent travel agencies compete to offer our site visitors the best cruise deal available in Europe.

Here is a short video that explains what one of our competitors does; it gives a good overview as our site will be similar:
http://www.voyabidder.com/video_how_voyabidder_works.php
(Voyabidder.com is not a great website in terms of design, so please dont get me wrong.)

The logo has already been created, but both the colours (should remain blueish) and the font can be modified. The font colour can be changed dramatically if you think this is of advantage.

The Website design should be professional and unique and become an eye catcher. It must attract visitors of all age groups, a "wow-effect" is definitely a bonus.
Users should easily see what this website is about.

We need the following text on our homepage:

"Immer der beste Preis -
denn Reisebüros kämpfen um Sie!"
(means "Always the best rate - as travel agents compete offer the best deal")
This is a sort of headline.

We also need:

So funktioniert Wellenfuchsportal:
1. Wunschkreuzfahrt wählen
2. Angebote erhalten und vergleichen
3. Reisebüro kontaktieren und buchen

(This explains briefly how our system works.)

Aside banners maybe needed later for advertising.

Additions I need on the front page are:
- Login / Sign-Up / Your benefits
(I quite like the way it's done on http://www.lirmatimes.com, at the very top of the page)
- Recommendation-link
(for everything else: Pls. refer to wfp02.wellenfuchsportal.de
- 3 or 4 "top offers of the week"
(current format is not very appealing; offers can be displayed as on http://sailings.tripnuvo.com/affiliate/promo.rvlx?OfferID=DOLUMA27 or

A maritime look is surely an option here, as we focus on cruises. But maybe you can surprise me with a great idea.

I quite like the designs where basically one photo / picture is used.
Some examples which look great IMHO:
http://pell-works.artfolioz.com/art/Glint-Swimmers-519304826
http://quorvanwebdesign.artfolioz.com/art/Website-Design-736152940
The following designer has also done a great job:
http://pixelmaker4387.artfolioz.com/gallery/

ATTACHED:
- logo
- Glint-Swimmers Design .png
- Flyer we use to attract travel agencies
- photo we use for the flyer (we own the rights)

Please get in touch with me if there are any questions or if you require further details. I ll get back to all inquiries / messages as soon as possible, usually within a few hours... Feel free to ask technical questions, too, (if any), the developer will be of assistance.

Reason: I decided to extend the deadline to have more time to comment on your designs and allow you to submit a few more proposals.

Reason: Sorry, more time needed to comment on all designs. Apart from this, some designers asked for more time.

Dear All,

Thank you so much for all your proposals.
Later today I will have a decent internet connection connection again, so I will be able to finally comment on your ideas and visions.

Hopefully next week we can finalize this project. Feel free to submit more designs or ask any questions if there are any.
Remember: Wellenfuchsportal won't be an ordinary travel agent. It brings cruise holiday makers and travel agents together.

Best

Target Market(s)

Holidaymakers / potential cruise holiday makers between 20 and 80.

Industry/Entity Type

Advertising

Requirements
Should not have
• Design should not use old-style, serif fonts.

```html
<!DOCTYPE html>
<html lang="de">
<head>
<meta charset="utf-8">
<title>Wellenfuchsportal – Kreuzfahrten im Preisvergleich</title>
<link rel="stylesheet" href="https://fonts.googleapis.com/css2?family=Jost:wght@500;600;700&family=Arimo:wght@400;700&display=swap">
<style>
  :root {
    --sky-top: #2b5891;
    --sky-mid: #8eafd6;
    --sea: #1c4f95;
    --sea-deep: #0c2d66;
    --navy: #0f2f5e;
    --navy-dark: #0b264d;
    --ink: #1a3560;
    --panel: rgba(226, 233, 243, 0.88);
    --panel-line: #b7c4d6;
    --menu-text: #3c3f45;
    --footer-head: #5b9bd5;
    --footer-link: #e6edf6;
    --copy: #4a7fbf;
    --btn-top: #3b85c8;
    --btn-bottom: #17579c;
    --white: #ffffff;
  }
  * { box-sizing: border-box; margin: 0; padding: 0; }
  html, body { width: 1067px; height: 1200px; overflow: hidden; }
  body { font-family: "Arimo", Arial, sans-serif; color: var(--ink); }
  .page { position: relative; width: 1067px; height: 1200px; overflow: hidden; }
  .backdrop {
    position: absolute; inset: 0;
    background:
      radial-gradient(ellipse 320px 60px at 180px 95px, rgba(255,255,255,.45), transparent 70%),
      radial-gradient(ellipse 260px 50px at 560px 120px, rgba(255,255,255,.35), transparent 70%),
      radial-gradient(ellipse 140px 160px at 1030px 280px, rgba(255,255,255,.6), transparent 70%),
      radial-gradient(ellipse 120px 90px at 30px 330px, rgba(255,255,255,.5), transparent 70%),
      radial-gradient(ellipse 700px 120px at 530px 1000px, rgba(235,240,246,.55), transparent 70%),
      linear-gradient(180deg, var(--sky-top) 0%, #4f7bb3 12%, var(--sky-mid) 28%, #a8c0dc 33%, #2c5ea3 37%, #174a8e 60%, var(--sea-deep) 100%);
  }

  /* top bar */
  .topbar { position: absolute; left: 0; top: 0; width: 1067px; height: 22px; background: var(--navy); }
  .topbar a { position: absolute; top: 5px; font: 600 10px "Jost", sans-serif; color: var(--white); text-decoration: none; letter-spacing: .5px; }
  .dome { position: absolute; left: 328px; top: -40px; width: 407px; height: 129px; border-radius: 0 0 203px 203px / 0 0 80px 80px; background: var(--navy); }
  .brand { position: absolute; left: 400px; top: 32px; display: flex; align-items: center; gap: 9px; }
  .brand-dot { width: 28px; height: 28px; border-radius: 50%; background: #e9f1fa; }
  .brand-name { font: 700 22px "Jost", sans-serif; color: #e9f1fa; letter-spacing: .5px; }

  /* main menu */
  .menu { position: absolute; left: 133px; top: 124px; width: 800px; height: 42px; background: var(--white); }
  .menu-inner { position: absolute; left: 4px; top: 4px; right: 4px; bottom: 4px; background: linear-gradient(#f6f7f8, #e9ebee); }
  .menu a { position: absolute; top: 12px; font: 500 10px "Jost", sans-serif; color: var(--menu-text); text-decoration: none; letter-spacing: .5px; white-space: nowrap; }

  /* slider */
  .slider { position: absolute; left: 133px; top: 178px; width: 800px; height: 283px; background: rgba(120, 135, 160, 0.7); }
  .slide-photo { position: absolute; left: 9px; top: 9px; width: 783px; height: 266px;
    background:
      radial-gradient(ellipse 330px 90px at 470px 150px, rgba(250,250,252,.95), transparent 75%),
      linear-gradient(180deg, #a99fb8 0%, #cfc8d6 30%, #e4e6ea 55%, #56b7bd 78%, #2a9aa6 100%); }
  .slide-quote { position: absolute; left: 27px; top: 206px; font: 700 29px/29px "Jost", sans-serif; color: var(--white); text-transform: uppercase; text-shadow: 0 1px 3px rgba(0,0,0,.55); }
  .slide-arrow { position: absolute; top: 136px; width: 27px; height: 27px; }

  /* panels */
  .panel { position: absolute; background: var(--panel); }
  .panel h2 { position: absolute; font: 700 20px "Jost", sans-serif; color: var(--ink); letter-spacing: .3px; }
  .rule { position: absolute; height: 1px; background: var(--panel-line); }
  .copy-text { position: absolute; font-size: 11.6px; line-height: 14px; color: #22344f; }

  .photo-frame { position: absolute; background: #8d99ab; }
  .photo { position: absolute; }

  /* offers */
  .offer { position: absolute; width: 380px; height: 92px; }
  .offer .photo { left: 0; top: 0; width: 133px; height: 92px; }
  .offer-title { position: absolute; left: 143px; top: 0; width: 240px; font: 700 11px/14px "Arimo", sans-serif; color: var(--ink); }
  .offer-sub { position: absolute; left: 143px; top: 46px; font: 700 9.5px "Arimo", sans-serif; color: var(--ink); }
  .offer-date { position: absolute; left: 143px; top: 58px; font: 400 9.5px "Arimo", sans-serif; color: #3d4b5f; }
  .offer-price { position: absolute; left: 145px; top: 74px; font: 700 15px "Arimo", sans-serif; color: var(--ink); }
  .offer-btn { position: absolute; left: 252px; top: 69px; width: 108px; height: 22px; background: linear-gradient(var(--btn-top), var(--btn-bottom)); clip-path: polygon(0 0, 92% 0, 100% 50%, 92% 100%, 0 100%); border-radius: 3px 0 0 3px; font: 700 10.5px/22px "Arimo", sans-serif; color: var(--white); padding-left: 9px; }

  /* footer */
  .footer { position: absolute; left: 0; top: 1031px; width: 1067px; height: 169px; background: var(--navy); }
  .footer-col { position: absolute; top: 22px; }
  .footer-col h3 { font: 700 12px "Arimo", sans-serif; color: var(--footer-head); margin-bottom: 7px; letter-spacing: .3px; }
  .footer-col a { display: block; font: 400 10px/15px "Arimo", sans-serif; color: var(--footer-link); text-decoration: none; }
  .footer-divider { position: absolute; top: 8px; width: 1px; height: 108px; background: #08203f; }
  .footer-base { position: absolute; left: 0; top: 130px; width: 1067px; height: 1px; background: #08203f; }
  .copyright { position: absolute; left: 134px; top: 142px; font: 400 10px "Arimo", sans-serif; color: var(--copy); }
  .social { position: absolute; top: 139px; width: 15px; height: 15px; border-radius: 2px; }
</style>
</head>
<body>
<div class="page">
  <div class="backdrop" role="img" aria-label="Photo background: blue sky with clouds over the open sea, seen from a cruise ship deck"></div>

  <header>
    <div class="topbar">
      <a href="#" style="left:152px">HOME</a>
      <a href="#" style="left:207px">ABOUT</a>
      <a href="#" style="left:263px">HELP</a>
      <a href="#" style="left:836px">LOG IN</a>
      <a href="#" style="left:881px">SIGN UP</a>
    </div>
    <div class="dome"></div>
    <div class="brand"><span class="brand-dot"></span><span class="brand-name">WELLENFUCHSPORTAL</span></div>

    <nav class="menu">
      <div class="menu-inner">
        <a href="#" style="left:15px">SO GEHTS</a>
        <a href="#" style="left:95px">ANGEBOTE ERHALTEN</a>
        <a href="#" style="left:228px">KREUZFAHRTSUCHE</a>
        <a href="#" style="left:346px">REEDEREIEN UND SCHIFFE</a>
        <a href="#" style="left:494px">SPECIALS</a>
        <a href="#" style="left:562px">KONTAKT</a>
        <a href="#" style="left:634px">FEHLERMELDUNG</a>
        <a href="#" style="left:735px">TRACKING</a>
      </div>
    </nav>
  </header>

  <section class="slider">
    <div class="slide-photo" role="img" aria-label="Photo: large white cruise ship with red funnel moored in turquoise water"></div>
    <svg class="slide-arrow" style="left:15px" viewBox="0 0 27 27"><circle cx="13.5" cy="13.5" r="13.5" fill="#fff"/><path d="M15.5 7.5 L9.5 13.5 L15.5 19.5" fill="none" stroke="#333" stroke-width="3"/></svg>
    <svg class="slide-arrow" style="left:758px" viewBox="0 0 27 27"><circle cx="13.5" cy="13.5" r="13.5" fill="#fff"/><path d="M11.5 7.5 L17.5 13.5 L11.5 19.5" fill="none" stroke="#333" stroke-width="3"/></svg>
    <p class="slide-quote">"Immer der beste Preis -<br>denn Reisebüros kämpfen um Sie!"</p>
  </section>

  <section class="panel" style="left:133px;top:483px;width:567px;height:209px">
    <h2 style="left:10px;top:8px">WELCOME</h2>
    <div class="rule" style="left:10px;top:39px;width:547px"></div>
    <div class="photo-frame" style="left:12px;top:54px;width:198px;height:130px">
      <div class="photo" style="left:8px;top:8px;width:182px;height:113px;background:radial-gradient(ellipse 80px 22px at 100px 72px,rgba(245,248,252,.9),transparent 75%),linear-gradient(180deg,#1f5fc4 0%,#4a88d8 55%,#1e4f9a 70%,#123c80 100%)" role="img" aria-label="Photo: white cruise ship sailing on deep blue sea"></div>
    </div>
    <p class="copy-text" style="left:219px;top:53px;width:340px">Sed ut perspiciatis unde omnis iste natus error sit voluptatem accusanti lum dolque laudantium, totam rem aperiam, eaque ipsa quae ab illo inventorritatis et liasi architecto beatae vitae dicta sunt explicabo. Nemo eni enim psam voluptatem quivoluptas sit aspernatur aut odit aut fugit, sed quia conseuuntur magni dolores e qui ratione voluptatem sequi nesciunt. Neque porrouisquam est, qui dolorem ipsuia dolor sit amet, consectetur, adipisci velit, sed quia non numquam eius modi teliora incidunt ut labore et dolore mailimualiquam quaerat voluptatem. Ut enim ad ima veniam, quis nostrum eitationem ullam corporis suscipit labori-</p>
  </section>

  <section class="panel" style="left:717px;top:483px;width:217px;height:209px">
    <h2 style="left:10px;top:8px">ABOUT US</h2>
    <div class="rule" style="left:10px;top:39px;width:197px"></div>
    <p class="copy-text" style="left:10px;top:52px;width:203px">Sed ut perspiciatis unde omnis iste naturror sit voluptatem accusanti lum dolque laudantium, totam rem aperiam, eaque ipsa que ab illo inventorritatis et liasi architecto beataitae dicta sunt explicabo. Nemo eni enim psaluptatem quivoluptas sit aspernatur aut odit aut fugit, sed quia conseuuntur magni dolores e qui ratione voluptatem sequi nesciunt.</p>
  </section>

  <section class="panel" style="left:133px;top:714px;width:800px;height:294px">
    <h2 style="left:10px;top:10px">SPECIAL OFFERS</h2>

    <article class="offer" style="left:22px;top:60px">
      <div class="photo" style="background:radial-gradient(ellipse 60px 20px at 66px 50px,rgba(250,250,250,.9),transparent 75%),linear-gradient(180deg,#b9c7d6 0%,#d9dee3 55%,#5a7288 80%,#3c5670 100%)" role="img" aria-label="Photo: cruise ship at sea"></div>
      <p class="offer-title">Inkl. Flügen mit Aeroluna, Transfers &amp; Hotelübernachtung in Buenos Aires</p>
      <p class="offer-sub">22 Tage Südamerika Kreuzfahrt</p>
      <p class="offer-date">Termin Juli 2012</p>
      <p class="offer-price">ab € 2.899</p>
      <div class="offer-btn">Angebot Bestellen</div>
    </article>

    <article class="offer" style="left:418px;top:60px">
      <div class="photo" style="background:linear-gradient(180deg,#c9ced4 0%,#8d949c 45%,#b29576 75%,#7d6349 100%)" role="img" aria-label="Photo: promenade deck of a cruise ship"></div>
      <p class="offer-title">Inkl. Flügen mit Aeroluna, Transfers &amp; Hotelübernachtung in Buenos Aires</p>
      <p class="offer-sub">22 Tage Südamerika Kreuzfahrt</p>
      <p class="offer-date">Termin Juli 2012</p>
      <p class="offer-price">ab € 2.899</p>
      <div class="offer-btn">Angebot Bestellen</div>
    </article>

    <article class="offer" style="left:22px;top:186px">
      <div class="photo" style="background:linear-gradient(160deg,#2a8fd0 0%,#e9eef3 45%,#1b6fb5 70%,#0e4c8d 100%)" role="img" aria-label="Photo: white cruise ship on bright blue water"></div>
      <p class="offer-title">Inkl. Flügen mit Aeroluna, Transfers &amp; Hotelübernachtung in Buenos Aires</p>
      <p class="offer-sub">22 Tage Südamerika Kreuzfahrt</p>
      <p class="offer-date">Termin Juli 2012</p>
      <p class="offer-price">ab € 2.899</p>
      <div class="offer-btn">Angebot Bestellen</div>
    </article>

    <article class="offer" style="left:418px;top:186px">
      <div class="photo" style="background:linear-gradient(180deg,#4fa7d8 0%,#9ccbe6 35%,#eef3f6 55%,#2fa3c3 80%,#1a86ab 100%)" role="img" aria-label="Photo: cruise ship with red funnel on turquoise sea"></div>
      <p class="offer-title">Inkl. Flügen mit Aeroluna, Transfers &amp; Hotelübernachtung in Buenos Aires</p>
      <p class="offer-sub">22 Tage Südamerika Kreuzfahrt</p>
      <p class="offer-date">Termin Juli 2012</p>
      <p class="offer-price">ab € 2.899</p>
      <div class="offer-btn">Angebot Bestellen</div>
    </article>
  </section>

  <footer class="footer">
    <div class="footer-col" style="left:143px">
      <h3>ÜBER UNS</h3>
      <a href="#">Über Wellenfuchsportal.de</a>
      <a href="#">Jobs</a>
      <a href="#">Partner</a>
      <a href="#">Werbung auf Wellenfuchsportal.de</a>
    </div>
    <div class="footer-divider" style="left:321px"></div>
    <div class="footer-col" style="left:342px">
      <h3>PRESSE</h3>
      <a href="#">Pressematerial</a>
      <a href="#">Wellenfuchsportal in den Medien</a>
      <a href="#">Pressemitteilungen</a>
      <a href="#">Wellenfuchsportal und die Sozialen Medien</a>
    </div>
    <div class="footer-divider" style="left:552px"></div>
    <div class="footer-col" style="left:567px">
      <h3>HILFE &amp; SERVICE</h3>
      <a href="#">Kundenmeinungen</a>
      <a href="#">Kontakt</a>
      <a href="#">FAQ's</a>
    </div>
    <div class="footer-divider" style="left:739px"></div>
    <div class="footer-col" style="left:777px">
      <h3>RECHTLICHES</h3>
      <a href="#">Disclaimer / Haftungsausschluss</a>
      <a href="#">Nutzungsbedingungen</a>
      <a href="#">Impressum</a>
    </div>
    <div class="footer-base"></div>
    <p class="copyright">© 2010-2012 Wellenfuchsportal.de</p>
    <span class="social" style="left:856px;background:#3a5a98"></span>
    <span class="social" style="left:877px;background:#3fa6d6"></span>
    <span class="social" style="left:897px;background:#2673ad"></span>
    <span class="social" style="left:918px;background:#e8811f"></span>
  </footer>
</div>
</body>
</html>
```